Larkspur Stillness

Logo picture and I want it to say

yoga. meditation. sound healing

small sweet classes

Larkspur-stillness.com

2740 West Hollander Ave Suite K
Alder Cove ca 93512

```html
<!DOCTYPE html>
<html lang="en">
<head>
<meta charset="utf-8">
<title>Larkspur Stillness – Flyer</title>
<link rel="stylesheet" href="https://fonts.googleapis.com/css2?family=Montserrat:wght@400;500&family=Questrial&display=swap">
<style>
  :root {
    --page-bg: #e4e4e4;
    --violet: #6a6cb6;
    --orchid: #c981b7;
    --blush-light: #fbf1f7;
    --blush-deep: #efbddd;
    --ink: #2e2e33;
    --frame-line: #55555c;
    --white: #ffffff;
    --photo-top: #dcd7d0;
    --photo-mid: #cdc9c3;
    --photo-floor: #9fa8ad;
  }
  * { margin: 0; padding: 0; box-sizing: border-box; }
  html, body {
    width: 1200px;
    height: 1200px;
    overflow: hidden;
    background: var(--page-bg);
  }
  .flyer {
    position: absolute;
    left: 189px;
    top: 20px;
    width: 821px;
    height: 1160px;
    overflow: hidden;
    isolation: isolate;
    background: radial-gradient(ellipse at 50% 55%, var(--blush-light) 0%, #f7e2f0 45%, var(--blush-deep) 100%);
    font-family: "Montserrat", sans-serif;
  }
  .flyer-art {
    position: absolute;
    inset: 0;
    width: 821px;
    height: 1160px;
  }
  .brand-mark {
    position: absolute;
    left: 592px;
    top: 491px;
    width: 176px;
    height: 176px;
    border: 2px solid var(--white);
    border-radius: 50%;
    display: flex;
    align-items: center;
    justify-content: center;
    text-align: center;
    color: var(--white);
    font-weight: 500;
    font-size: 21px;
    line-height: 1.2;
  }
  .services {
    position: absolute;
    left: 0;
    right: 0;
    top: 776px;
    text-align: center;
    color: var(--violet);
    font-weight: 400;
    font-size: 36px;
    white-space: nowrap;
  }
  .services .divider { padding: 0 6px; }
  .tagline {
    position: absolute;
    left: 0;
    right: 0;
    top: 829px;
    text-align: center;
    color: var(--orchid);
    font-size: 45px;
    font-weight: 400;
  }
  .web-pill {
    position: absolute;
    left: 185px;
    top: 907px;
    width: 451px;
    height: 51px;
    border-radius: 26px;
    background: var(--violet);
    color: var(--white);
    font-size: 29px;
    display: flex;
    align-items: center;
    justify-content: center;
  }
  .web-pill::after {
    content: "";
    position: absolute;
    left: 80px;
    right: 80px;
    bottom: -14px;
    height: 12px;
    border-radius: 50%;
    background: rgba(60, 40, 60, 0.28);
    filter: blur(6px);
    z-index: -1;
  }
  .address {
    position: absolute;
    left: 199px;
    top: 1002px;
    width: 421px;
    height: 96px;
    border: 1px solid var(--frame-line);
    border-top: none;
    border-radius: 0 0 4px 4px;
    display: flex;
    flex-direction: column;
    align-items: center;
    justify-content: center;
    padding-top: 4px;
    font-family: "Questrial", sans-serif;
    font-size: 24px;
    line-height: 1.3;
    color: var(--ink);
  }
  .address::before,
  .address::after {
    content: "";
    position: absolute;
    top: 0;
    width: 191px;
    height: 1px;
    background: var(--frame-line);
  }
  .address::before { left: -1px; }
  .address::after { right: -1px; }
  .address-pin {
    position: absolute;
    top: -16px;
    left: 50%;
    width: 20px;
    height: 28px;
    margin-left: -10px;
  }
</style>
</head>
<body>
  <div class="flyer">
    <svg class="flyer-art" viewBox="0 0 1055 1490" preserveAspectRatio="none">
      <defs>
        <linearGradient id="photoTone" x1="0" y1="0" x2="0" y2="1">
          <stop offset="0" stop-color="#dcd7d0"/>
          <stop offset="0.55" stop-color="#cdc9c3"/>
          <stop offset="1" stop-color="#9fa8ad"/>
        </linearGradient>
      </defs>
      <path class="class-photo" role="img"
        aria-label="Photo: a small group of people meditating cross-legged on yoga mats in a bright studio"
        fill="url(#photoTone)"
        d="M0 0 H1055 V600 L499 778 C360 700 150 700 0 752 Z"/>
      <path class="wave-orchid" fill="var(--orchid)"
        d="M39 760 C150 700 380 690 499 778 C380 865 150 860 39 760 Z"/>
      <path class="wave-violet" fill="var(--violet)"
        d="M499 778 C700 660 880 560 1055 568 V925 C900 965 760 915 630 852 C580 828 535 800 499 778 Z"/>
    </svg>

    <div class="brand-mark">Larkspur<br>Stillness</div>

    <p class="services">YOGA<span class="divider">|</span>MEDITATION<span class="divider">|</span>SOUND HEALING</p>
    <p class="tagline">Small Sweet Classes</p>

    <div class="web-pill">Larkspur-stillness.com</div>

    <div class="address">
      <svg class="address-pin" viewBox="0 0 20 28" aria-hidden="true">
        <path d="M10 1 C4.8 1 1 4.9 1 9.8 C1 16.5 10 27 10 27 C10 27 19 16.5 19 9.8 C19 4.9 15.2 1 10 1 Z" fill="var(--orchid)"/>
        <circle cx="10" cy="10" r="3.6" fill="#f6dff0"/>
      </svg>
      <span>2740 West Hollander Ave Suite K</span>
      <span>Alder Cove ca 93512</span>
    </div>
  </div>
</body>
</html>
```